New Webpage for High Class Expert Witness Services Company

We are looking for a minimalist design for a webpage that just has our logo and an entry form offer to connect with one of our Liaisons.
The entry form should just ask for Name, Email, Contact Info and Description of Project.

Company Name is: The Marlow Crest Advisory Services

Number of Pages Required

1 page

```html
<!DOCTYPE html>
<html lang="en">
<head>
<meta charset="UTF-8">
<title>Marlow Crest Advisory Services — Connect with a Liaison</title>
<link href="https://fonts.googleapis.com/css2?family=Poppins:wght@400;500;700&family=Tinos&display=swap" rel="stylesheet">
<style>
  :root {
    --ink-dark: #121212;
    --ink: #2a2a2a;
    --muted: #555;
    --placeholder: #8a8a8a;
    --line: #7a7a7a;
    --field-border: #9a9a9a;
    --paper: #ffffff;
    --light-text: #f2f2f2;
    --silver: #d8d8d8;
  }
  * { box-sizing: border-box; margin: 0; padding: 0; }
  html, body { width: 699px; height: 1200px; overflow: hidden; background: var(--paper); }
  body { position: relative; font-family: 'Poppins', sans-serif; color: var(--ink); }

  .hero { position: absolute; top: 0; left: 0; width: 699px; height: 271px; background: var(--ink-dark); text-align: center; }
  .brand-name { font-family: 'Tinos', serif; font-size: 17px; letter-spacing: 1px; color: var(--silver); text-transform: uppercase; }
  .hero .brand-name { position: absolute; top: 30px; left: 0; width: 100%; }
  .hero-title {
    position: absolute; top: 92px; left: 0; width: 100%;
    font-family: 'Tinos', serif; font-weight: 400; font-size: 31px; line-height: 35px;
    background: linear-gradient(180deg, #ffffff 0%, #9c9c9c 100%);
    -webkit-background-clip: text; background-clip: text; color: transparent;
  }
  .hero-lead { position: absolute; top: 173px; left: 0; width: 100%; font-size: 9.5px; line-height: 16.5px; color: var(--light-text); }

  .connector { position: absolute; left: 349px; width: 1px; background: var(--ink); }
  .connector.top { top: 246px; height: 51px; }
  .connector.bottom { top: 790px; height: 52px; background: var(--line); }

  .liaison-panel {
    position: absolute; top: 343px; left: 132px; width: 435px; height: 448px;
    border: 1px solid var(--line); border-top: none;
    background: linear-gradient(160deg, #ffffff 0%, #f4f4f6 50%, #ffffff 100%);
  }
  .panel-edge { position: absolute; top: 343px; height: 1px; background: var(--ink); }
  .panel-edge.left { left: 132px; width: 53px; }
  .panel-edge.right { left: 511px; width: 56px; }
  .panel-title {
    position: absolute; top: 324px; left: 0; width: 699px; text-align: center;
    font-family: 'Tinos', serif; font-size: 32px; font-weight: 400;
    background: linear-gradient(180deg, #2a2a2a 0%, #6a6a6a 100%);
    -webkit-background-clip: text; background-clip: text; color: transparent;
  }
  .panel-lead { position: absolute; top: 369px; left: 0; width: 699px; text-align: center; font-size: 9.5px; line-height: 16.5px; color: var(--ink); }

  .field-label { position: absolute; font-size: 8px; color: var(--ink); }
  .field {
    position: absolute; height: 27px; border: 1px solid var(--field-border); background: var(--paper);
    font-size: 8px; color: var(--placeholder); padding-left: 14px; line-height: 25px;
  }
  .field.textarea { height: 100px; line-height: 1; padding-top: 10px; }
  .dial-code {
    position: absolute; top: 0; left: 0; width: 60px; height: 25px; background: #ebebeb;
    border-right: 1px solid var(--field-border); display: flex; align-items: center; gap: 6px; padding-left: 7px; color: var(--ink);
  }
  .phone-number { position: absolute; left: 79px; top: 0; }

  .submit-button {
    position: absolute; top: 733px; left: 277px; width: 146px; height: 28px;
    background: linear-gradient(90deg, #3a3a3c 0%, #000 45%, #000 100%);
    color: #fff; font-weight: 700; font-size: 8.5px; text-align: center; line-height: 28px; letter-spacing: 0.1px;
  }

  .trust-statement {
    position: absolute; top: 914px; left: 0; width: 699px; text-align: center;
    font-family: 'Tinos', serif; font-size: 18.5px; line-height: 25px; color: var(--muted);
  }

  .site-footer { position: absolute; top: 1038px; left: 0; width: 699px; height: 162px; background: var(--ink-dark); color: #fff; }
  .site-footer .brand-name { position: absolute; top: 42px; left: 63px; width: 160px; font-size: 11px; line-height: 13px; }
  .footer-link { position: absolute; top: 45px; font-size: 11px; color: #fff; }
  .footer-link.email { left: 0; width: 699px; text-align: center; }
  .footer-link.privacy { right: 65px; }
  .footer-rule { position: absolute; top: 104px; left: 63px; width: 570px; height: 1px; background: #444; }
  .copyright { position: absolute; top: 127px; left: 0; width: 699px; text-align: center; font-size: 9px; }
</style>
</head>
<body>
  <header class="hero">
    <div class="brand-name">Marlow Crest Advisory Services</div>
    <h1 class="hero-title">Seamless Medical Expert<br>Integration</h1>
    <p class="hero-lead">Expert witness coordination for complex defense matters—delivered<br>with precision, speed, and discretion.</p>
  </header>

  <div class="connector top"></div>

  <section class="liaison-panel"></section>
  <div class="panel-edge left"></div>
  <div class="panel-edge right"></div>
  <h2 class="panel-title">Connect with a Liaison</h2>
  <p class="panel-lead">Submit your case details and a Marlow Crest Advisory Services liaison will<br>respond promptly to coordinate the appropriate medical expert support.</p>

  <span class="field-label" style="top:428px;left:168px;">First Name</span>
  <div class="field" style="top:445px;left:169px;width:178px;">Jhon</div>
  <span class="field-label" style="top:428px;left:352px;">Last Name</span>
  <div class="field" style="top:445px;left:353px;width:178px;">Smith</div>

  <span class="field-label" style="top:484px;left:168px;">Email Address</span>
  <div class="field" style="top:500px;left:169px;width:362px;">Jhon123@email.com</div>

  <span class="field-label" style="top:539px;left:168px;">Contact Number</span>
  <div class="field" style="top:555px;left:169px;width:362px;padding-left:0;">
    <div class="dial-code">
      <svg width="18" height="12" viewBox="0 0 18 12" aria-hidden="true">
        <rect width="18" height="12" fill="#b22234"/>
        <g fill="#fff"><rect y="1.7" width="18" height="1"/><rect y="3.7" width="18" height="1"/><rect y="5.7" width="18" height="1"/><rect y="7.7" width="18" height="1"/><rect y="9.7" width="18" height="1"/></g>
        <rect width="8" height="6.5" fill="#3c3b6e"/>
      </svg>
      <span>+1</span>
      <svg width="7" height="5" viewBox="0 0 7 5" aria-hidden="true"><path d="M1 1l2.5 2.5L6 1" stroke="#333" fill="none" stroke-width="1"/></svg>
    </div>
    <span class="phone-number">888-888-8888</span>
  </div>

  <span class="field-label" style="top:595px;left:168px;">Project Description</span>
  <div class="field textarea" style="top:611px;left:169px;width:362px;">Type here...</div>

  <div class="submit-button">SUBMIT REQUEST</div>

  <div class="connector bottom"></div>

  <p class="trust-statement">Trusted in high-stakes medical-legal evaluations,<br>delivering objective, well-researched expert opinions<br>that support timely case resolution.</p>

  <footer class="site-footer">
    <div class="brand-name">Marlow Crest<br>Advisory Services</div>
    <span class="footer-link email">inquiries@marlowcrest.example</span>
    <span class="footer-link privacy">Privacy &amp; Confidentiality</span>
    <div class="footer-rule"></div>
    <p class="copyright">2026 Marlow Crest Advisory Services. All Rights Reserved.</p>
  </footer>
</body>
</html>
```